Australian Software Consultancy needs new Business Card Design

Design Business Card based on existing design artefacts (attached). We are open to all designs. As its a 2 sided design and we thought it might be quite striking to have one side with a black background and te other side with a white background.

Target Market(s)

Financial Services mainly.

Industry/Entity Type

Business

Contact Information for Business Card

Name :
Position :
Email :

Requirements
Must have
• Funky design using our existing assets

```html
<!DOCTYPE html>
<html lang="en">
<head>
<meta charset="utf-8">
<title>Northvale Business Card</title>
<link href="https://fonts.googleapis.com/css2?family=Open+Sans:wght@400;600;700&display=swap" rel="stylesheet">
<style>
  :root {
    --page: #e9e6e1;
    --card: #262626;
    --card-edge: #1d1d1d;
    --red: #e8202c;
    --red-soft: #f2777b;
    --text-grey: #5a5a5a;
    --watermark: #2e2e2e;
    --contact: #a9a9a9;
  }
  html, body {
    margin: 0;
    width: 1200px;
    height: 800px;
    overflow: hidden;
    background: var(--page);
    font-family: "Open Sans", Arial, sans-serif;
  }
  .canvas {
    position: relative;
    width: 1200px;
    height: 800px;
  }
  .card {
    position: absolute;
    top: 245px;
    width: 540px;
    height: 310px;
    background: var(--card);
    border-radius: 16px;
    box-shadow: 0 10px 28px rgba(0,0,0,0.25);
    overflow: hidden;
  }
  .card--front { left: 40px; }
  .card--back { left: 620px; }

  /* Front */
  .brand {
    position: absolute;
    inset: 0;
    display: flex;
    align-items: center;
    justify-content: center;
    gap: 18px;
  }
  .brand__dot {
    width: 74px;
    height: 74px;
    border-radius: 50%;
    border: 6px solid var(--red);
    box-sizing: border-box;
  }
  .brand__name {
    font-weight: 600;
    font-size: 40px;
    letter-spacing: 2px;
    color: var(--red);
  }

  /* Back */
  .watermark {
    position: absolute;
    right: 40px;
    top: 28px;
    width: 190px;
    height: 190px;
    border-radius: 50%;
    border: 16px solid var(--watermark);
    box-sizing: border-box;
  }
  .back-brand {
    position: absolute;
    right: 58px;
    top: 104px;
    font-weight: 600;
    font-size: 28px;
    letter-spacing: 1.5px;
    color: var(--red-soft);
  }
  .person {
    position: absolute;
    left: 0;
    top: 34px;
    padding-left: 34px;
    border-left: 12px solid var(--red);
    margin-left: 0;
  }
  .person__name {
    margin: 0;
    font-weight: 700;
    font-size: 26px;
    line-height: 1.05;
    color: var(--text-grey);
  }
  .person__title {
    margin: 2px 0 0;
    font-weight: 600;
    font-size: 15px;
    color: var(--red);
  }
  .contact {
    position: absolute;
    left: 40px;
    top: 198px;
    margin: 0;
    padding: 0;
    list-style: none;
    font-size: 15px;
    color: var(--contact);
  }
  .contact li {
    display: flex;
    align-items: center;
    gap: 8px;
    height: 22px;
  }
  .contact svg { width: 14px; height: 14px; fill: var(--red-soft); }
  .rule {
    position: absolute;
    left: 0;
    top: 0;
  }
  .website {
    position: absolute;
    left: 40px;
    top: 268px;
    font-size: 16px;
    color: var(--red);
  }
</style>
</head>
<body>
<main class="canvas">
  <section class="card card--front">
    <div class="brand">
      <span class="brand__dot"></span>
      <span class="brand__name">NORTHVALE</span>
    </div>
  </section>

  <section class="card card--back">
    <div class="watermark"></div>
    <div class="back-brand">NORTHVALE</div>

    <div class="person">
      <p class="person__name">Your Name</p>
      <p class="person__title">Job Title</p>
    </div>

    <ul class="contact">
      <li>
        <svg viewBox="0 0 16 16" aria-hidden="true"><path d="M1 6 Q8 0 15 6 L13 8 L11 6 L11 5 Q8 4 5 5 L5 6 L3 8 Z M4 9 H12 L13 15 H3 Z"/></svg>
        000 000 0000
      </li>
      <li>
        <svg viewBox="0 0 16 16" aria-hidden="true"><path d="M1 3 H15 V13 H1 Z M2 4 L8 9 L14 4" stroke="#262626" stroke-width="1.2"/></svg>
        youremail@xyz.com
      </li>
    </ul>

    <svg class="rule" width="540" height="310" viewBox="0 0 540 310" aria-hidden="true">
      <polyline points="0,258 400,258 440,222 540,222" fill="none" stroke="var(--red)" stroke-width="3"/>
      <polygon points="440,218 540,218 540,230 432,230" fill="var(--red-soft)"/>
    </svg>

    <div class="website">yourwebsite.com</div>
  </section>
</main>
</body>
</html>
```